Weight loss surgery restaurant card

We need to create a card for patients who have undergone weight loss surgery to take to restaurants so they can request smaller meals. These patients have had surgery on their stomach so that they can only consume half to one cup of food at a time. So normal sized restaurant meals are way too big (and cost a lot). This card they can present to the restaurant to communicate the fact that they have had weight loss surgery and therefore request a smaller meal portion at reduced cost

Target Market(s)

Restaurants serving weight loss surgery patients

Industry/Entity Type

Health Care

Contact Information for Business Card

This will be a plastic card similar to business card size.

Requirements
Must have
• The front of the card should include the following text:
• The individual bearing this card has undergone weight loss surgery.
• This surgery restricts portion sizes to between half and one cup of food at a time.
• Please give consideration to allowing smaller portions of your regular meals to be ordered to reduce wastage and excess costs.
• Example: a half size portion priced at two thirds of usual cost.
• The back of the card will have spaces for the person to write certain information. These are the categories that can be filled in by hand:
• Name:
• Procedure performed:
• Date of procedure (month/year):
• Treating Clinic Name:
• Treating Clinic Signature:
• Somewhere down the bottom should be something along the lines of:
• supplied from bernardwhitlow.com.au
Nice to have
• A nice design with imagery/colours etc ... not just the text on a white background! Bright attractive colours preferred.
• I have uploaded my logo ... a roughly triangular image followed by my name etc. The triangular logo image could be used somewhere on the card and this logo can be interchangeable for other clinics who purchase the card.
• **Please note that I don't want my name to be included as part of the logo on the card ... just use the triangular image on the side of the logo without the following name**
• Also, the colouring of the card does not have to reflect my logo colours as I am anticipating interchanging this logo with other logos if other clinics choose to adopt the card. I am interested to see other, more generic, colour choices as well as my logo colours

```html
<!DOCTYPE html>
<html lang="en">
<head>
<meta charset="utf-8">
<title>Bernard Whitlow – Restaurant Portion Card</title>
<link href="https://fonts.googleapis.com/css2?family=Cinzel:wght@400;600&family=Quicksand:wght@400;500&display=swap" rel="stylesheet">
<style>
  :root {
    --teal: #0e857b;
    --teal-dark: #0a6d65;
    --ink: #5c6166;
    --line-grey: #b9bcbf;
    --paper: #ffffff;
    --mist: #e9eced;
    --backdrop: #2a2a2b;
  }
  html, body {
    margin: 0;
    padding: 0;
    width: 1200px;
    height: 880px;
    overflow: hidden;
    background: var(--backdrop);
  }
  .canvas {
    position: relative;
    width: 1200px;
    height: 880px;
  }
  .card {
    position: absolute;
    width: 560px;
    height: 353px;
    border-radius: 22px;
    overflow: hidden;
    background: var(--paper);
    box-shadow: 0 10px 30px rgba(0,0,0,.45);
    font-family: "Quicksand", sans-serif;
  }

  /* Front */
  .card--front { left: 60px; top: 60px; }
  .front__band {
    position: absolute; left: 0; top: 0; bottom: 0;
    width: 92px;
    background: var(--teal);
  }
  .front__rule {
    position: absolute; left: 98px; top: 0; bottom: 0;
    width: 2px;
    background: var(--line-grey);
  }
  .front__decor {
    position: absolute; right: 40px; top: -20px;
    width: 220px; height: 330px;
    border-radius: 50%;
    background: radial-gradient(ellipse at center, var(--mist) 0%, rgba(233,236,237,.55) 45%, rgba(255,255,255,0) 72%);
  }
  .front__content {
    position: absolute; left: 128px; right: 30px; top: 28px;
  }
  .brand { display: flex; align-items: center; gap: 12px; }
  .brand__dot {
    width: 34px; height: 34px; border-radius: 50%;
    background: var(--teal); flex: none;
  }
  .brand__name {
    font-family: "Cinzel", serif; font-weight: 600;
    font-size: 30px; line-height: 1; color: var(--teal);
    letter-spacing: .5px;
  }
  .brand__role {
    font-family: "Cinzel", serif; font-weight: 400;
    font-size: 10.5px; color: var(--ink);
    letter-spacing: 1.4px; margin-top: 4px;
  }
  .facts {
    list-style: none; margin: 18px 0 0 46px; padding: 0;
    color: var(--ink); font-size: 13.5px; line-height: 1.3;
  }
  .facts li { margin-bottom: 7px; padding-left: 10px; text-indent: -10px; }

  /* Back */
  .card--back { left: 580px; top: 460px; }
  .back__strip {
    position: absolute; left: 0; top: 0; bottom: 0;
    width: 130px; background: var(--paper);
  }
  .back__brand {
    position: absolute; left: 65px; top: 176px;
    transform: translate(-50%, -50%) rotate(-90deg);
    white-space: nowrap; text-align: left;
  }
  .back__brand .brand__name { font-size: 30px; }
  .back__panel {
    position: absolute; left: 130px; top: 0; right: 0; bottom: 0;
    background: var(--teal);
    color: #fff;
    padding: 40px 34px 0 30px;
    overflow: hidden;
  }
  .back__decor {
    position: absolute; right: 20px; top: 10px;
    width: 200px; height: 330px;
    border-radius: 50%;
    background: radial-gradient(ellipse at center, rgba(255,255,255,.22) 0%, rgba(255,255,255,.1) 45%, rgba(255,255,255,0) 72%);
  }
  .fields { position: relative; list-style: none; margin: 0; padding: 0; font-size: 15px; }
  .field {
    display: flex; align-items: flex-end; gap: 4px;
    height: 30px;
  }
  .field__fill {
    flex: 1; border-bottom: 2px dotted rgba(255,255,255,.85);
    margin-bottom: 5px;
  }
  .back__site {
    position: absolute; left: 30px; bottom: 34px;
    font-size: 16px; letter-spacing: 1px;
  }
</style>
</head>
<body>
<main class="canvas">

  <section class="card card--front" aria-label="Card front">
    <div class="front__band"></div>
    <div class="front__rule"></div>
    <div class="front__decor" role="img" aria-label="Faint soft grey swoosh background decoration"></div>
    <div class="front__content">
      <div class="brand">
        <span class="brand__dot"></span>
        <div>
          <div class="brand__name">Bernard Whitlow</div>
          <div class="brand__role">GENERAL, UPPER GI &amp; BARIATRIC SURGEON</div>
        </div>
      </div>
      <ul class="facts">
        <li>- The individual bearing this card has undergone weight loss surgery.</li>
        <li>- Around 500,000 of these procedures are performed around the world every year.</li>
        <li>- This surgery restricts portion sizes to between half and one cup of food at a time.</li>
        <li>- Please give consideration to allowing smaller portions of your regular meals to be ordered to reduce wastage and excess costs.</li>
        <li>- Example: a half size portion priced at two thirds of usual cost.</li>
      </ul>
    </div>
  </section>

  <section class="card card--back" aria-label="Card back">
    <div class="back__strip">
      <div class="back__brand">
        <div class="brand__name">Bernard Whitlow</div>
        <div class="brand__role">GENERAL, UPPER GI &amp; BARIATRIC SURGEON</div>
      </div>
    </div>
    <div class="back__panel">
      <div class="back__decor" role="img" aria-label="Faint translucent swoosh background decoration"></div>
      <ul class="fields">
        <li class="field">- Name:<span class="field__fill"></span></li>
        <li class="field">- Procedure performed:<span class="field__fill"></span></li>
        <li class="field">- Date of procedure (month/year):<span class="field__fill"></span></li>
        <li class="field">- Treating Clinic Name:<span class="field__fill"></span></li>
        <li class="field">- Treating Clinic Signature:<span class="field__fill"></span></li>
        <li class="field"><span class="field__fill"></span></li>
        <li class="field"><span class="field__fill"></span></li>
      </ul>
      <div class="back__site">www.bernardwhitlow.com.au</div>
    </div>
  </section>

</main>
</body>
</html>
```